Pool Builder Website Design in arizona

Our current site is located here: kelvaro.net

We are looking to give this a modern facelift. We will be cutting your design into a wordpress theme so we can utilize the CMS plateform backend.

Look and Feel
• Clean cut and professional
• Mobile friendly
• Updated from old site
• Feel intrigued but relax (do you have trust logos? Marla looking into this)
Colors
• Warm tropical neutral colors
• Orange, brown, blues
- Please make the site modern and more sleek look that looks like a 2015 style design and NOT 1999.
- Must be coded as a wordpress theme
- must create a home page, inner page and blog page
- must allow client to BLOG using the post section in wordpress

This pool company is a pool builder/installer in Phoenix arizona.

NOTE::: Please create a home page and one internal page.

Serif
Sans Serif

• - Must be coded as a wordpress theme
• - must create a home page, inner page and blog page
• - must allow client to BLOG using the post section in wordpress

```html
<!DOCTYPE html>
<html lang="en">
<head>
<meta charset="utf-8">
<title>Saguaro Pools</title>
<link href="https://fonts.googleapis.com/css2?family=Roboto:wght@400;500;700&family=Oswald:wght@400&display=swap" rel="stylesheet">
<style>
:root{
  --blue:#1f5fb4;
  --blue-dark:#124a9a;
  --nav-top:#2a6fc7;
  --nav-bottom:#1651a5;
  --green:#8cc63f;
  --footer:#2f6cb7;
  --footer-bottom:#111;
  --ink:#222;
  --grey:#555;
  --white:#fff;
}
*{margin:0;padding:0;box-sizing:border-box}
html,body{width:728px;height:1200px;overflow:hidden}
body{position:relative;background:var(--white);font-family:'Roboto',Arial,sans-serif;color:var(--ink)}
.abs{position:absolute}
.sky-backdrop{left:0;top:0;width:728px;height:411px;background:linear-gradient(180deg,#6f9ccc 0%,#b7cfe6 45%,#5d86ad 75%,#2d5f9a 100%)}
.header{left:53px;top:0;width:621px;height:80px;background:var(--white)}
.brand{left:74px;top:22px;display:flex;align-items:center;gap:6px;font-size:19px;font-weight:700;color:var(--blue)}
.brand-mark{width:14px;height:14px;border-radius:50%;background:var(--green)}
.phone{left:416px;top:39px;display:flex;align-items:center;gap:6px;font-size:10px;color:var(--ink)}
.search{left:529px;top:35px;width:128px;height:22px;border:1px solid #cfcfcf;background:var(--white);font-size:8.5px;color:var(--ink);padding:6px 7px}
.search-btn{left:635px;top:35px;width:22px;height:22px;background:#4a86d0;display:flex;align-items:center;justify-content:center}
.nav{left:53px;top:80px;width:621px;height:38px;background:linear-gradient(180deg,var(--nav-top),var(--nav-bottom));display:flex}
.nav a{color:var(--white);text-decoration:none;font-size:10.5px;display:flex;align-items:center;justify-content:center;border-right:1px solid rgba(0,0,0,.18)}
.nav a.active{background:var(--green);color:#1d2a10}
.hero{left:53px;top:118px;width:621px;height:340px;background:linear-gradient(180deg,#6d8f4a 0%,#8a8a70 40%,#3fc3d0 68%,#2fb0c4 82%,#b89a7a 92%,#a58767 100%)}
.hero-shadow{left:100px;top:458px;width:528px;height:14px;background:radial-gradient(ellipse at top,rgba(0,0,0,.22),transparent 70%)}
.caption{left:53px;top:290px;width:338px;height:60px;background:rgba(30,30,30,.78);color:var(--white);font-family:'Oswald',sans-serif;font-size:28px;line-height:60px;padding-left:19px}
.arrow{top:362px;width:22px;height:22px;border-radius:50%;background:var(--white);display:flex;align-items:center;justify-content:center}
.welcome-title{left:0;top:490px;width:728px;text-align:center;font-size:16px;font-weight:500}
.welcome-title span{color:var(--blue)}
.welcome-text{left:56px;top:519px;width:616px;text-align:center;font-size:8.2px;line-height:14px;color:var(--grey);letter-spacing:-0.05px}
.portfolio-band{left:0;top:589px;width:728px;height:252px;background:linear-gradient(180deg,#1d2634 0%,#27313b 55%,#1d3a5a 80%,#232a30 100%)}
.portfolio-title{left:0;top:607px;width:728px;text-align:center;font-size:19px;font-weight:700;color:var(--green)}
.portfolio-sub{left:0;top:640px;width:728px;text-align:center;font-size:13px;color:var(--white)}
.thumb{top:673px;width:188px;height:131px;border:3px solid var(--white)}
.feature-img{left:48px;top:858px;width:213px;height:139px;border:3px solid var(--white);box-shadow:0 0 3px rgba(0,0,0,.45);background:linear-gradient(180deg,#5d7e3a 0%,#7a9a5a 28%,#27a9e6 45%,#1e8fd8 75%,#c9b99a 100%)}
.sizes-title{left:274px;top:862px;font-size:14.5px;font-weight:500}
.sizes-title span{color:var(--blue)}
.sizes-text{left:275px;top:885px;width:402px;font-size:9.2px;line-height:15.4px;color:var(--grey);letter-spacing:-0.1px}
.read-more{left:275px;top:971px;width:63px;height:21px;background:#222;color:var(--white);font-size:7.5px;display:flex;align-items:center;justify-content:center;border-radius:2px}
.footer{left:0;top:1015px;width:728px;height:137px;background:var(--footer);color:var(--white)}
.footer h3{position:absolute;top:20px;font-size:11px;font-weight:400}
.f-text{font-size:7px;line-height:12px;position:absolute}
.news-thumb{width:36px;height:29px;border:1.5px solid var(--white);background:linear-gradient(180deg,#1f2d3c,#2f6aa0);position:absolute}
.social{position:absolute;display:flex;align-items:center;gap:13px;font-size:7.5px}
.social i{width:20px;height:20px;border:1.5px solid rgba(255,255,255,.8);border-radius:50%;display:block}
.news-meta{position:absolute;font-size:7px;line-height:11px}
.news-meta b{font-weight:500;display:block;font-size:7.2px}
.news-meta small{font-size:5.8px}
.mail{position:absolute;left:511px;top:1090px;width:129px;height:20px;background:var(--white);color:#888;font-size:6.5px;padding:6px 7px}
.join{position:absolute;left:640px;top:1090px;width:34px;height:20px;background:#111;color:var(--white);font-size:7px;font-weight:700;display:flex;align-items:center;justify-content:center}
.bottom-bar{left:0;top:1152px;width:728px;height:48px;background:var(--footer-bottom);color:#ddd;font-size:7px;text-align:center;line-height:48px}
</style>
</head>
<body>
<div class="abs sky-backdrop" role="img" aria-label="Sky with clouds over a poolside edge"></div>
<header class="abs header"></header>
<div class="abs brand"><span class="brand-mark"></span>Saguaro Pools</div>
<div class="abs phone">
  <svg width="12" height="12" viewBox="0 0 24 24"><circle cx="12" cy="12" r="11" fill="none" stroke="#3a7cc9" stroke-width="1.6"/><path d="M8 7c1-1 2 0 2.5 1.5s-1 1.5-.5 2.5 1.5 2.5 2.5 3 1-1 2.5-.5 2.5 1.5 1.5 2.5c-2 2-5 0-7-2s-3.5-5-1.5-7z" fill="#3a7cc9"/></svg>
  +61 (0)2 5550 1734
</div>
<div class="abs search">Search..</div>
<div class="abs search-btn"><svg width="11" height="11" viewBox="0 0 24 24"><circle cx="10" cy="10" r="6.5" fill="none" stroke="#fff" stroke-width="2.5"/><path d="M15 15l6 6" stroke="#fff" stroke-width="3"/></svg></div>
<nav class="abs nav">
  <a class="active" href="#" style="width:73px">HOME</a>
  <a href="#" style="width:88px">ABOUT US</a>
  <a href="#" style="width:71px">STYLE</a>
  <a href="#" style="width:93px">PORTFOLIO</a>
  <a href="#" style="width:110px">INSTALLATION</a>
  <a href="#" style="width:100px;border-right:0">CONTACT US</a>
</nav>
<div class="abs hero" role="img" aria-label="Backyard fiberglass pool in front of a two-storey house with garden and rock feature"></div>
<div class="abs hero-shadow"></div>
<div class="abs caption">The Fiberglass Pool Experts!</div>
<div class="abs arrow" style="left:78px"><svg width="10" height="10" viewBox="0 0 10 10"><path d="M6.5 1.5L3 5l3.5 3.5" fill="none" stroke="#222" stroke-width="1.4"/></svg></div>
<div class="abs arrow" style="left:105px"><svg width="10" height="10" viewBox="0 0 10 10"><path d="M3.5 1.5L7 5 3.5 8.5" fill="none" stroke="#222" stroke-width="1.4"/></svg></div>

<h1 class="abs welcome-title">WELCOME TO &nbsp;<span>SAGUARO POOLS</span></h1>
<p class="abs welcome-text">Lorem Ipsum has been the industry's standard dummy text ever since the 1500s, when an unknown printer took a galley of type and scrambled it to make a type specimen book. It has survived not only five centuries, but also the leap into electronic typesetting, remaining essentially unchanged &nbsp;Lorem Ipsum has been the industry's standard dummy text ever since the 1500s, when an unknown printer took a galley of type and scrambled it to make a type specimen book.</p>

<section class="abs portfolio-band" role="img" aria-label="Dim evening view of a backyard pool"></section>
<h2 class="abs portfolio-title">PORTFOLIO</h2>
<p class="abs portfolio-sub">Lorem Ipsum is simply dummy text of the printing and typesetting industry</p>
<div class="abs thumb" style="left:57px;background:linear-gradient(180deg,#2a2a24 0%,#3cc4d8 35%,#2eb2cf 65%,#b9a595 85%,#9c8c80 100%)" role="img" aria-label="Freeform pool with rock waterfall"></div>
<div class="abs thumb" style="left:271px;background:linear-gradient(180deg,#1b1b1b 0%,#0f3f8a 40%,#1a56a8 70%,#c09a8c 90%,#8a7e78 100%)" role="img" aria-label="Deep blue pool with rock water feature"></div>
<div class="abs thumb" style="left:482px;background:linear-gradient(180deg,#8a7562 0%,#b59c86 35%,#a86a4a 55%,#23407e 70%,#b08a78 100%)" role="img" aria-label="Oval pool beside a house wall"></div>

<div class="abs feature-img" role="img" aria-label="Rectangular blue pool with steel ladder"></div>
<h2 class="abs sizes-title">SIZES AND <span>STYLES</span></h2>
<p class="abs sizes-text">Lorem Ipsum has been the industry's standard dummy text ever since the 1500s, when an unknown printer took a galley of type and scrambled it to make a type specimen book. It has survived not only five centuries, but also the leap into electronic typesetting, remaining essentially unchanged. It was popularised in the 1960s with the release of Typeset sheets containing Lorem Ipsum passages, and more recently with desktop publishing software like PageLayout including versions</p>
<div class="abs read-more">READ MORE</div>

<footer class="abs footer">
  <h3 style="left:55px">CONTACT INFO</h3>
  <p class="f-text" style="left:54px;top:50px;width:135px">Lorem ipsum dolor sit amet, consectetur adipisicing elit, sed do eiusmod tempor incididunt ut labore et dolore magna</p>
  <p class="f-text" style="left:55px;top:92px">(555) 0100 246810</p>
  <p class="f-text" style="left:54px;top:109px">info@kelvaro.net</p>

  <h3 style="left:228px">LATEST NEWS</h3>
  <div class="news-thumb" style="left:230px;top:48px"></div>
  <div class="news-meta" style="left:272px;top:51px"><b>Crew receive award</b><small>july 7, 2015</small></div>
  <div class="news-thumb" style="left:230px;top:90px"></div>
  <div class="news-meta" style="left:272px;top:93px"><b>Crew receive award</b><small>july 7, 2015</small></div>

  <h3 style="left:392px">FOLLOW US ON</h3>
  <div class="social" style="left:391px;top:48px"><i></i>Pagebook</div>
  <div class="social" style="left:391px;top:75px"><i></i>Chirper</div>
  <div class="social" style="left:391px;top:101px"><i></i>Snapgram</div>

  <h3 style="left:511px;top:19px">NEWSLETTER</h3>
  <p class="f-text" style="left:511px;top:44px;width:165px">Join our mailing list to stay up to date and get notices about our new releases!</p>
</footer>
<div class="mail">mail@example.com</div>
<div class="join">JOIN</div>
<div class="abs bottom-bar">© Copyright 2015 &nbsp; All Rights Reserved</div>
</body>
</html>
```